Tech business card design

We need an amazing business card design for our new business 'Vantry' a marketing tech startup based in Sydney, Australia. We provide an online marketplace for businesses to search and buy advertising media, connect with service providers and learn more about marketing. We wish to communicate 'cool tech', reliability and professionalism and design based around our logo.

Target Market(s)

Business Owners

Contact Information for Business Card

Name
Position
Email Address
Website
Phone Number

Font styles to use
Other font styles liked:
• Avenir & Avenir Next

Colors

Designer to choose colors to be used in the design.

```html
<!DOCTYPE html>
<html lang="en">
<head>
<meta charset="utf-8">
<title>Vantry Business Card</title>
<link rel="stylesheet" href="https://fonts.googleapis.com/css2?family=Nunito+Sans:wght@400;700;800;900&display=swap">
<style>
  :root {
    --page-bg: #e9e9ec;
    --navy: #141a45;
    --navy-deep: #151a4a;
    --navy-soft: #2c305f;
    --back-top: #161b4c;
    --back-bottom: #1e2458;
    --paper: #ffffff;
    --ink-muted: #2a2e4a;
    --ghost: #f0f1f4;
  }
  * { margin: 0; padding: 0; box-sizing: border-box; }
  html, body {
    width: 1200px; height: 1200px; overflow: hidden;
    background: var(--page-bg);
    font-family: "Nunito Sans", "Avenir Next", Avenir, sans-serif;
  }
  .card {
    position: absolute;
    left: 210px;
    width: 768px;
    height: 439px;
    border-radius: 24px;
    overflow: hidden;
    box-shadow: 0 10px 24px rgba(0,0,0,0.18);
  }
  /* Front */
  .card-front { top: 134px; background: var(--paper); }
  .front-wordmark {
    position: absolute; right: 52px; top: 14px;
    font-size: 104px; font-weight: 900; letter-spacing: -2px;
    color: var(--navy); line-height: 1;
  }
  .ghost-wordmark {
    position: absolute; right: 40px; top: 286px;
    font-size: 142px; font-weight: 900; letter-spacing: -3px;
    color: var(--ghost); line-height: 1;
  }
  .name-accent {
    position: absolute; left: 0; top: 202px;
    width: 13px; height: 52px; background: var(--navy);
  }
  .person-name {
    position: absolute; left: 26px; top: 195px;
    font-size: 31px; font-weight: 800; color: var(--navy);
    letter-spacing: 0.5px;
  }
  .person-role {
    position: absolute; left: 27px; top: 236px;
    font-size: 18px; font-weight: 400; color: var(--ink-muted);
  }
  .contact-rule {
    position: absolute; left: 27px; top: 324px;
    width: 2px; height: 86px; background: var(--navy);
  }
  .contact-list { list-style: none; position: absolute; left: 48px; top: 320px; }
  .contact-item {
    display: flex; align-items: center; height: 34px;
    font-size: 19px; color: var(--navy);
  }
  .contact-icon { width: 16px; height: 16px; margin-right: 14px; flex: none; }
  .front-band { position: absolute; left: 0; bottom: 0; width: 768px; height: 12px; }
  /* Back */
  .card-back {
    top: 622px;
    background: linear-gradient(180deg, var(--back-top), var(--back-bottom));
  }
  .back-glow { position: absolute; inset: 0; }
  .back-wordmark {
    position: absolute; left: 0; right: 0; top: 118px;
    text-align: center;
    font-size: 158px; font-weight: 900; letter-spacing: -3px;
    color: var(--paper); line-height: 1;
  }
  .back-url {
    position: absolute; left: 0; right: 0; top: 382px;
    text-align: center;
    font-size: 18px; font-weight: 800; letter-spacing: 1.5px;
    color: #e8e9f0;
  }
</style>
</head>
<body>
  <section class="card card-front">
    <div class="front-wordmark">Vantry</div>
    <div class="ghost-wordmark">Vantry</div>
    <div class="name-accent"></div>
    <h1 class="person-name">LIAM CARTER</h1>
    <p class="person-role">Director</p>
    <div class="contact-rule"></div>
    <ul class="contact-list">
      <li class="contact-item">
        <svg class="contact-icon" viewBox="0 0 16 16"><rect x="3.5" y="0.5" width="9" height="15" rx="1.5" fill="var(--navy)"/><rect x="5" y="2.5" width="6" height="9" fill="#fff"/><circle cx="8" cy="13.4" r="0.9" fill="#fff"/></svg>
        000.000.0000
      </li>
      <li class="contact-item">
        <svg class="contact-icon" viewBox="0 0 16 16"><rect x="1" y="3.5" width="14" height="10" rx="1" fill="var(--navy)"/><path d="M1.5 4.2 L8 9 L14.5 4.2" stroke="#fff" stroke-width="1.2" fill="none"/></svg>
        lcarter@vantry.com
      </li>
      <li class="contact-item">
        <svg class="contact-icon" viewBox="0 0 16 16" fill="none" stroke="var(--navy)" stroke-width="1.4"><circle cx="8" cy="8" r="6.5"/><ellipse cx="8" cy="8" rx="2.8" ry="6.5"/><path d="M1.5 8h13M2.6 4.5h10.8M2.6 11.5h10.8"/></svg>
        www.vantry.com
      </li>
    </ul>
    <svg class="front-band" viewBox="0 0 768 12" preserveAspectRatio="none">
      <polygon points="0,0 375,0 363,12 0,12" fill="var(--navy-deep)"/>
      <polygon points="387,0 768,0 768,12 375,12" fill="var(--navy-soft)"/>
    </svg>
  </section>

  <section class="card card-back">
    <svg class="back-glow" viewBox="0 0 768 439" preserveAspectRatio="none">
      <path d="M0,262 Q384,150 768,262 L768,439 L0,439 Z" fill="rgba(255,255,255,0.04)"/>
    </svg>
    <div class="back-wordmark">Vantry</div>
    <div class="back-url">www.vantry.com</div>
  </section>
</body>
</html>
```